Biz Card Design TPVC

New business card for a new company.
Logo was completed by a designer on ArtFlock and looking to continue requesting additional services.
Company Name: Tidal Prime Voltage Collective
Although this company is starting in Canada, we will be moving towards a global presence within the next 6 months.
Key elements to this business are as follows.
Energy Procurement
Energy Reduction Services
Demand Side Consulting
Energy Efficiency Consulting
Saving Clients Money
Helping Them Go "Green"
Managing Their Energy Requirements
Basically the goal for our company is to find the best procurement solution for our clients and reduce their energy consumption. This reduces their expenses and the amount of greenhouse gas they produce on a daily basis.
I have been in the energy footprint for the last 20 years and know that most companies are looking to "do whatever is necessary to get them to sign on the dotted line". I would prefer to walk away from a client that I can't help than to put them into a situation that they will regret for years to come. This is where the "TIDAL" part of the company name comes from.
The following is a catch phrase that encompasses what we do.
"Reducing your carbon footprint & energy bill at the same time!"
The back of the card needs to have this statement along with some sort of illustration. The back is a playground for creative ideas.
The front of the card needs the following.
Logo.
First & Last Name (Gus Marwick)
Title (Energy Warrior)
Phone Number (555) 314-2768
Fax Number (555) 862-4091
Email Address gus@tidalprimevoltage.example
Address 47 Orchard Lane Toronto Ontario K4P 2Z7
I want it to be a card that is remembered when any of my staff give it to a customer. It HAS to stand out.
Target Market(s)
Business Owners, Decision Makers, 30 to 65+
Industry/Entity Type
Business
Look and feel
Each slider illustrates characteristics of the customer's brand and the style your logo design should communicate.

```html
<!DOCTYPE html>
<html lang="en">
<head>
<meta charset="utf-8">
<title>Tidal Prime Voltage Collective – Business Card</title>
<link href="https://fonts.googleapis.com/css2?family=Questrial&display=swap" rel="stylesheet">
<style>
  :root {
    --green: #1f9a4c;
    --green-soft: rgba(91, 191, 74, .16);
    --green-faint: rgba(91, 191, 74, 0);
    --blue: #3d6fc2;
    --ink: #1d1d1d;
    --paper: #ffffff;
    --backdrop: #ecebe8;
    --font: "Questrial", "Century Gothic", sans-serif;
  }
  * { box-sizing: border-box; margin: 0; padding: 0; }
  html, body { width: 1200px; height: 900px; overflow: hidden; }
  body {
    background: var(--backdrop);
    font-family: var(--font);
    display: flex; flex-direction: column; align-items: center; justify-content: center;
    gap: 48px;
  }
  .card {
    position: relative;
    width: 640px; height: 366px;
    background: var(--paper);
    box-shadow: 0 6px 18px rgba(0,0,0,.18);
    overflow: hidden;
  }
  .card-sweep { position: absolute; inset: 0; }

  /* wordmark */
  .wordmark {
    position: absolute; display: flex; align-items: center; gap: 10px;
    color: var(--blue); font-size: 24px; letter-spacing: -.2px; white-space: nowrap;
  }
  .wordmark-dot { width: 16px; height: 16px; border-radius: 50%; background: var(--green); flex: none; }
  .front .wordmark { left: 210px; top: 120px; }

  /* contact list */
  .contact-list { position: absolute; left: 96px; top: 212px; list-style: none; }
  .contact-item {
    display: flex; align-items: center; gap: 10px;
    font-size: 15px; color: var(--ink); height: 27px;
  }
  .contact-icon {
    width: 20px; height: 20px; border-radius: 4px; background: var(--green);
    display: inline-flex; align-items: center; justify-content: center; flex: none;
  }
  .contact-icon svg { width: 13px; height: 13px; fill: #fff; }
  .contact-fax { margin-left: 26px; display: inline-flex; align-items: center; gap: 10px; }

  .person { position: absolute; right: 58px; top: 232px; text-align: left; }
  .person-name { font-size: 23px; color: var(--ink); }
  .person-title { font-size: 17px; color: var(--green); margin-top: 2px; }

  /* back */
  .back-illustration {
    position: absolute; left: 70px; top: 30px; width: 520px; height: 300px;
    border-radius: 50%;
    background: radial-gradient(ellipse at center, var(--green-soft) 0%, var(--green-faint) 70%);
  }
  .back .wordmark { left: 50%; top: 130px; transform: translateX(-50%); font-size: 32px; gap: 14px; }
  .back .wordmark-dot { width: 22px; height: 22px; }
  .tagline {
    position: absolute; left: 0; right: 0; top: 190px;
    text-align: center; font-size: 17px; color: var(--green);
  }
  .web-address { position: absolute; right: 40px; bottom: 30px; font-size: 17px; color: var(--ink); }
  .web-address .tone-blue { color: var(--blue); }
  .web-address .tone-green { color: var(--green); }
</style>
</head>
<body>

<section class="card front" aria-label="Card front">
  <svg class="card-sweep" viewBox="0 0 640 366" aria-hidden="true">
    <path d="M0 0 H300 C160 40 62 180 40 366 H0 Z" fill="var(--green)"/>
    <path d="M316 0 C172 44 74 184 54 366" fill="none" stroke="var(--blue)" stroke-width="7"/>
  </svg>

  <div class="wordmark"><span class="wordmark-dot"></span>Tidal Prime Voltage Collective</div>

  <ul class="contact-list">
    <li class="contact-item">
      <span class="contact-icon"><svg viewBox="0 0 16 16"><path d="M8 2 1 8h2v6h4v-4h2v4h4V8h2z"/></svg></span>
      47 Orchard Lane Toronto Ontario K4P 2Z7
    </li>
    <li class="contact-item">
      <span class="contact-icon"><svg viewBox="0 0 16 16"><path d="M4 1h3l1 4-2 1c1 2 2 3 4 4l1-2 4 1v3c0 1-1 2-2 2C7 14 2 9 2 3c0-1 1-2 2-2z"/></svg></span>
      (555) 314-2768
      <span class="contact-fax">
        <span class="contact-icon"><svg viewBox="0 0 16 16"><path d="M4 1h8v4H4zM2 6h12v7H2zM5 8h2v1H5zm4 0h2v1H9zm-4 2h2v1H5zm4 0h2v1H9z"/></svg></span>
        (555) 862-4091
      </span>
    </li>
    <li class="contact-item">
      <span class="contact-icon"><svg viewBox="0 0 16 16"><path d="M8 1a7 7 0 1 0 4 12.7l-.8-1.2A5.6 5.6 0 1 1 13.6 8v.8c0 .8-.5 1.3-1.1 1.3s-1-.5-1-1.3V5h-1.3v.6A3 3 0 1 0 10.8 10a2.4 2.4 0 0 0 4.2-1.2V8A7 7 0 0 0 8 1zm0 8.7A1.7 1.7 0 1 1 8 6.3a1.7 1.7 0 0 1 0 3.4z"/></svg></span>
      gus@tidalprimevoltage.example
    </li>
    <li class="contact-item">
      <span class="contact-icon"><svg viewBox="0 0 16 16"><path d="M8 1a7 7 0 1 0 0 14A7 7 0 0 0 8 1zm4.9 6h-2a11 11 0 0 0-.8-4A5.6 5.6 0 0 1 12.9 7zM8 2.5c.6.8 1.3 2.4 1.4 4.5H6.6C6.7 4.9 7.4 3.3 8 2.5zM5.9 3a11 11 0 0 0-.8 4h-2a5.6 5.6 0 0 1 2.8-4zM3.1 8.5h2a11 11 0 0 0 .8 4 5.6 5.6 0 0 1-2.8-4zM8 13.5c-.6-.8-1.3-2.4-1.4-5h2.8c-.1 2.6-.8 4.2-1.4 5zm2.1-1a11 11 0 0 0 .8-4h2a5.6 5.6 0 0 1-2.8 4z"/></svg></span>
      www.tidalprimevoltage.example
    </li>
  </ul>

  <div class="person">
    <p class="person-name">Gus Marwick</p>
    <p class="person-title">Energy Warrior</p>
  </div>
</section>

<section class="card back" aria-label="Card back">
  <div class="back-illustration" role="img" aria-label="Soft green energy-and-nature illustration behind the company name"></div>
  <div class="wordmark"><span class="wordmark-dot"></span>Tidal Prime Voltage Collective</div>
  <p class="tagline">Reducing your carbon footprint &amp; energy bill at the same time!</p>
  <p class="web-address">www.<span class="tone-blue">tidal</span><span class="tone-green">primevoltage</span>.example</p>
</section>

</body>
</html>
```